Velmar Ops Business Cards

We need to design some upbeat business cards. We are an Industrial Rope Access Company/Height Safety Company that specialize in Rope Access, Confined Space, Anchor Points, Safety Systems, PPE Inspecions and Rigging.
Company name is Velmar Ops Ltd
Card is for Gareth Lomas the Company Director
His mobile number is 027 418 9072 and email is gareth@velmarops.co.nz. Website address is www.velmarops.co.nz.
We will post some pictures below to ensure you get a good idea of what we do.

```html
<!DOCTYPE html>
<html lang="en">
<head>
<meta charset="utf-8">
<title>Velmar Ops Business Cards</title>
<link href="https://fonts.googleapis.com/css2?family=Oswald:wght@300;400;600&display=swap" rel="stylesheet">
<style>
  :root {
    --page: #e6e6e8;
    --card-black: #1c1a1b;
    --card-white: #ffffff;
    --band-grey: #a7a8aa;
    --ink-dark: #3a3a3c;
    --ink-light: #f2f2f2;
    --rule: #8c8c8c;
  }
  * { box-sizing: border-box; margin: 0; padding: 0; }
  html, body {
    width: 1200px; height: 1200px; overflow: hidden;
    background: var(--page);
    font-family: "Oswald", "Arial Narrow", sans-serif;
  }
  .sheet {
    width: 1200px; height: 1200px;
    display: flex; flex-direction: column; align-items: center; justify-content: center;
    gap: 60px;
  }
  .card {
    width: 900px; height: 514px;
    position: relative; overflow: hidden;
    box-shadow: 0 10px 30px rgba(0,0,0,.18);
  }

  /* Front */
  .card--front { background: var(--card-black); }
  .front__top {
    position: absolute; left: 0; top: 0; width: 100%; height: 232px;
    background: var(--card-white);
    display: flex; align-items: center; justify-content: center;
  }
  .wordmark {
    font-weight: 600; letter-spacing: 2px; line-height: 1;
  }
  .front__top .wordmark { color: var(--card-black); font-size: 108px; }
  .front__band {
    position: absolute; left: 0; top: 232px; width: 100%; height: 62px;
    background: var(--band-grey);
    display: flex; align-items: center; justify-content: center; gap: 14px;
    color: var(--ink-dark);
  }
  .person__name { font-size: 34px; font-weight: 300; }
  .person__divider { width: 2px; height: 32px; background: var(--ink-dark); }
  .person__role { font-size: 24px; font-weight: 400; }
  .front__contact {
    position: absolute; left: 0; top: 294px; width: 100%; height: 220px;
    display: flex; align-items: center; justify-content: center;
    color: var(--ink-light); font-weight: 300; font-size: 25px;
  }
  .contact__col { display: flex; flex-direction: column; gap: 10px; padding: 0 26px; }
  .contact__col--left { align-items: flex-end; text-align: right; }
  .contact__rule { width: 1px; height: 86px; background: var(--rule); }
  .contact__line { display: flex; align-items: center; gap: 10px; }
  .icon { width: 20px; height: 20px; fill: none; stroke: var(--ink-light); stroke-width: 1.6; }

  /* Back */
  .card--back {
    background: var(--card-black);
    display: flex; flex-direction: column; align-items: center;
    color: var(--ink-light); text-align: center;
  }
  .card--back .wordmark { color: var(--card-white); font-size: 112px; margin-top: 110px; }
  .services { margin-top: 52px; font-weight: 300; }
  .services__heading { font-size: 24px; letter-spacing: 1px; margin-bottom: 8px; }
  .services__list { font-size: 26px; line-height: 1.4; }
</style>
</head>
<body>
<main class="sheet">
  <section class="card card--front" aria-label="Business card front">
    <div class="front__top">
      <span class="wordmark">Velmar Ops</span>
    </div>
    <div class="front__band">
      <span class="person__name">Gareth Lomas</span>
      <span class="person__divider"></span>
      <span class="person__role">Director</span>
    </div>
    <div class="front__contact">
      <div class="contact__col contact__col--left">
        <span class="contact__line">Velmar Ops Ltd</span>
        <span class="contact__line">www.velmarops.co.nz
          <svg class="icon" viewBox="0 0 20 20" aria-hidden="true"><circle cx="10" cy="10" r="8"/><ellipse cx="10" cy="10" rx="3.5" ry="8"/><line x1="2" y1="10" x2="18" y2="10"/></svg>
        </span>
      </div>
      <span class="contact__rule"></span>
      <div class="contact__col">
        <span class="contact__line">
          <svg class="icon" viewBox="0 0 20 20" aria-hidden="true"><path d="M5 2l3 4-2 2c1 2.5 3.5 5 6 6l2-2 4 3-2 3C9 17 3 11 2 4z"/></svg>
          027 418 9072
        </span>
        <span class="contact__line">
          <svg class="icon" viewBox="0 0 20 20" aria-hidden="true"><rect x="2" y="4" width="16" height="12"/><path d="M2 4l8 7 8-7"/></svg>
          gareth@velmarops.co.nz
        </span>
      </div>
    </div>
  </section>

  <section class="card card--back" aria-label="Business card back">
    <span class="wordmark">Velmar Ops</span>
    <div class="services">
      <p class="services__heading">SPECIALIZE IN</p>
      <p class="services__list">Rope Access, Confined Space, Anchor Points<br>Safety Systems, PPE Inspecions and Rigging</p>
    </div>
  </section>
</main>
</body>
</html>
```